HIghly Competitive Dance School needs a web page make-over!!

Looking for a web design that captures our brand identity (Royal theme) that is New & Innovative and appeals to parents & children. I am open to creativity and want something original. Our color scheme is Burgundy & Gold with Black highlights. I currently use NetPerch and have up to 10 pages to publish.

Reason: I have run into some problems that have prevented me from making a selection; please bear with me.

Reason: To all the designers...I apologize for the delay but I am in the middle of fall registration and construction on a new building. I can return to this task on Monday but I am deep in the middle of back-to-school. Please forgive me for this very long delay. Thanks for your understanding!!

To all the designers...I apologize for the delay but I am in the middle of fall registration and construction on a new building. I can return to this task on Monday but I am deep in the middle of back-to-school. Please forgive me for this very long delay. Thanks for your understanding!!

Target Market(s)

Parents with young children who have a disposable income

Industry/Entity Type

School

Requirements
Must have
• Home Page
Classes
Policies/Guidelines
Our Staff (with pictures)
Contact Us (complete your info here)
Our Story (history page)
Gallery (pictures & Videos)
Registration Form (with coinloop feature)

```html
<!DOCTYPE html>
<html lang="en">
<head>
<meta charset="utf-8">
<title>Crownline Dance Studio</title>
<link href="https://fonts.googleapis.com/css2?family=Open+Sans:wght@300;400;600&family=Play&display=swap" rel="stylesheet">
<style>
:root{
  --burgundy:#84092f;
  --burgundy-dark:#4f0a20;
  --gold:#f5b84a;
  --gold-deep:#f0a93a;
  --black:#1b1b1d;
  --bar:#202022;
  --grey:#4a4a4a;
  --white:#ffffff;
  --muted:#9a9a9a;
}
*{box-sizing:border-box;margin:0;padding:0}
html,body{width:1200px;height:686px;overflow:hidden;background:var(--black)}
body{position:relative;font-family:"Open Sans",sans-serif;color:var(--white)}
.sidebar{position:absolute;left:0;top:0;width:170px;height:686px;background:linear-gradient(180deg,#7a0a2c 0%,#5e0a24 60%,#6c0a28 100%)}
.brand{position:relative;height:132px;background:linear-gradient(180deg,#5a5a5a,#454545);display:flex;flex-direction:column;align-items:center;justify-content:center;gap:4px}
.brand::after{content:"";position:absolute;left:75px;bottom:-12px;border-left:10px solid transparent;border-right:10px solid transparent;border-top:12px solid #454545}
.brand-mark{width:18px;height:18px;background:var(--burgundy)}
.brand-name{font-weight:600;font-size:19px;color:var(--gold);letter-spacing:1px}
.brand-sub{font-weight:400;font-size:9px;color:var(--gold);letter-spacing:1px}
.nav{position:absolute;left:18px;top:180px;width:135px;list-style:none;border-top:1px dotted var(--gold-deep)}
.nav li{height:31.3px;border-bottom:1px dotted var(--gold-deep);display:flex;align-items:center;font-family:"Play",sans-serif;font-size:11px;letter-spacing:.6px;color:var(--gold)}
.call{position:absolute;left:14px;top:477px}
.call-label{font-size:19px;line-height:22px}
.call-phone{font-size:22px;font-weight:600;color:var(--gold);line-height:28px}
.social{position:absolute;left:18px;top:568px;display:flex;gap:10px}
.social span{width:25px;height:25px;border-radius:50%;background:#a86a7c}
.copyright{position:absolute;left:18px;top:602px;font-size:10.5px;line-height:14px;width:145px}
.topbar{position:absolute;left:170px;top:0;width:1030px;height:56px;background:var(--black);border-bottom:1px dotted #777}
.search{position:absolute;left:72px;top:11px;height:34px;border-left:1px solid #555;padding-left:14px;display:flex;align-items:center;font-family:"Play",sans-serif;font-size:12px;color:var(--gold)}
.search-btn{position:absolute;right:0;top:0;width:56px;height:56px;background:var(--burgundy);display:flex;align-items:center;justify-content:center}
.hero{position:absolute;left:170px;top:57px;width:1030px;height:571px;background:linear-gradient(90deg,#3a0a1c 0%,#2a0c1e 25%,#0d1115 55%,#101a20 100%)}
.hero-photo{position:absolute;right:0;top:0;width:660px;height:571px;background:radial-gradient(ellipse at 55% 45%,#b9dbe6 0%,#6c98a8 28%,#1e2d35 62%,rgba(13,17,21,0) 85%)}
.hero-title{position:absolute;left:70px;top:375px;width:364px;height:58px;background:var(--burgundy);display:flex;align-items:center;padding-left:13px;font-size:28px;font-weight:400;letter-spacing:.5px}
.hero-sub{position:absolute;left:70px;top:443px;height:42px;padding:0 8px;background:rgba(0,0,0,.45);display:flex;align-items:center;font-size:21px;font-weight:300}
.player{position:absolute;left:170px;top:628px;width:1030px;height:58px;background:var(--bar);border-top:1px dotted var(--gold-deep)}
.track-thumb{position:absolute;left:70px;top:8px;width:40px;height:40px;background:linear-gradient(135deg,#777,#333)}
.track-title{position:absolute;left:125px;top:11px;font-size:11.5px;font-weight:600;color:#ccc}
.track-share{position:absolute;left:125px;top:34px;font-size:8.5px;color:var(--muted);text-decoration:underline;word-spacing:2px}
.controls{position:absolute;left:321px;top:13px}
.progress{position:absolute;left:403px;top:25px;width:162px;height:7px;background:#111;border:1px solid #444}
.progress i{display:block;width:62px;height:100%;background:var(--gold)}
.time{position:absolute;top:38px;font-size:8.5px;color:var(--muted)}
.volume{position:absolute;left:576px;top:25px;width:45px;height:6px;background:var(--gold)}
.btn{position:absolute;top:0;width:57px;height:58px;background:var(--burgundy);display:flex;align-items:center;justify-content:center}
</style>
</head>
<body>
<aside class="sidebar">
  <div class="brand">
    <span class="brand-mark"></span>
    <span class="brand-name">CROWNLINE</span>
    <span class="brand-sub">DANCE STUDIO</span>
  </div>
  <ul class="nav">
    <li>HOME</li><li>CLASSES</li><li>GUIDELINES</li><li>OUR STAFF</li><li>GALLERY</li><li>CONTACT</li><li>VIDEO</li><li>REGISTRATION</li>
  </ul>
  <div class="call">
    <div class="call-label">Call Us !</div>
    <div class="call-phone">555-014-2298</div>
  </div>
  <div class="social"><span></span><span></span><span></span><span></span></div>
  <p class="copyright">Copyright © Crownline Dance Studio 2013</p>
</aside>

<header class="topbar">
  <div class="search">Search...</div>
  <div class="search-btn">
    <svg width="30" height="30" viewBox="0 0 30 30"><circle cx="12" cy="12" r="8.5" fill="none" stroke="#f5b84a" stroke-width="3.5"/><line x1="18.5" y1="18.5" x2="27" y2="27" stroke="#f5b84a" stroke-width="4.5" stroke-linecap="round"/></svg>
  </div>
</header>

<section class="hero">
  <div class="hero-photo" role="img" aria-label="Four ballerinas in white tutus dancing en pointe on a dark stage"></div>
  <h1 class="hero-title">LOREM IPSUM DUMMY</h1>
  <p class="hero-sub">LOREM IPSUM DOLOR SIT AMET CONSECTEUR ADISCIPING</p>
</section>

<footer class="player">
  <div class="track-thumb" role="img" aria-label="Album cover"></div>
  <div class="track-title">Velmont-Nocturne For Strings</div>
  <div class="track-share">Share on Friendlane &nbsp;Share on Chirpline</div>
  <svg class="controls" width="80" height="34" viewBox="0 0 80 34">
    <circle cx="14" cy="17" r="13" fill="#f5b84a"/><circle cx="66" cy="17" r="13" fill="#f5b84a"/><circle cx="40" cy="17" r="17" fill="#f5b84a"/>
    <path d="M8 13v8M15 13l-6 4 6 4zM20 13l-6 4 6 4z" fill="#202022" stroke="#202022" stroke-width="1"/>
    <path d="M60 13l6 4-6 4zM65 13l6 4-6 4zM72 13v8" fill="#202022" stroke="#202022" stroke-width="1"/>
    <rect x="35" y="9" width="3" height="16" fill="#202022"/><rect x="42" y="9" width="3" height="16" fill="#202022"/>
  </svg>
  <div class="progress"><i></i></div>
  <span class="time" style="left:403px">00.02.53</span>
  <span class="time" style="left:525px">00.05.54</span>
  <div class="volume"></div>
  <div class="btn" style="left:916px">
    <svg width="34" height="26" viewBox="0 0 34 26"><path d="M2 7h8l12 12h8M2 19h8l12-12h8" fill="none" stroke="#f5b84a" stroke-width="3"/><path d="M27 2l6 5-6 5zM27 14l6 5-6 5z" fill="#f5b84a"/></svg>
  </div>
  <div class="btn" style="left:974px;width:56px">
    <svg width="32" height="26" viewBox="0 0 32 26"><rect y="2" width="32" height="4" fill="#f5b84a"/><rect y="11" width="32" height="4" fill="#f5b84a"/><rect y="20" width="32" height="4" fill="#f5b84a"/></svg>
  </div>
</footer>
</body>
</html>
```